MARLOWE COLLEGE BUILDING SIGNAGE

WE ARE A COLLEGE AND WE REQUIRE OUR BUILDING TO BE WELL PRENSENTED IN OUR BRAND SO IT LOOK APART AND STANDS OUT IN THE STREET.

WE HAVE ANOTHE COLLEGE NEXT TO US WHICH IS OUR COMPETITOR, WE WANT WALK IN TRAFFIC TO BE WALKING INTO OUR BUILDING .

SO WE WOULD LIKE TO PLACES SIGNS OR BANNERS ETC ON THE BUILDING TO GIVE IT A THEME, WE ARE UNABLE TO PAINT THE BUILDING AS ITS HERITAGE LISTED, I HAVE UP LOADED THE PICS

Target Market(s)

STUDENTS AGE OF 18 PLUS

Industry/Entity Type

College

```html
<!DOCTYPE html>
<html lang="en">
<head>
<meta charset="utf-8">
<title>Marlowe College Banner</title>
<link rel="stylesheet" href="https://fonts.googleapis.com/css2?family=Signika:wght@300;600&family=Open+Sans:ital,wght@1,400&display=swap">
<style>
  :root {
    --navy-deep: #0a1a2e;
    --navy: #14304f;
    --steel: #3f6f93;
    --glow: #cfeefb;
    --ice: #8fd3ee;
    --white: #ffffff;
  }
  html, body {
    margin: 0;
    padding: 0;
    overflow: hidden;
    background: var(--navy-deep);
  }
  .banner {
    position: relative;
    width: 1200px;
    height: 216px;
    overflow: hidden;
    background:
      radial-gradient(ellipse 520px 260px at 190px 108px, rgba(143, 211, 238, 0.55), rgba(63, 111, 147, 0.35) 45%, rgba(20, 48, 79, 0) 75%),
      linear-gradient(90deg, var(--steel) 0%, var(--navy) 45%, var(--navy-deep) 100%);
  }
  .banner__bulb {
    position: absolute;
    left: 0;
    top: 0;
    width: 360px;
    height: 216px;
  }
  .banner__text {
    position: absolute;
    left: 480px;
    top: 0;
    width: 580px;
    height: 216px;
    text-align: center;
    color: var(--white);
  }
  .banner__name {
    margin: 0;
    position: absolute;
    left: 0;
    right: 0;
    top: 22px;
    font-family: "Signika", sans-serif;
    font-weight: 600;
    font-size: 50px;
    line-height: 56px;
    letter-spacing: 0.5px;
  }
  .banner__tagline {
    margin: 0;
    position: absolute;
    left: 0;
    right: 0;
    top: 80px;
    font-family: "Signika", sans-serif;
    font-weight: 300;
    font-size: 29px;
    line-height: 34px;
  }
  .banner__fields {
    margin: 0;
    position: absolute;
    left: 0;
    right: 0;
    top: 163px;
    font-family: "Open Sans", sans-serif;
    font-style: italic;
    font-weight: 400;
    font-size: 23px;
    line-height: 30px;
  }
</style>
</head>
<body>
  <div class="banner">
    <svg class="banner__bulb" viewBox="0 0 360 216" role="img" aria-label="Glowing light bulb with rays of light">
      <defs>
        <radialGradient id="bulb-glow" cx="0.5" cy="0.55" r="0.5">
          <stop offset="0" stop-color="var(--white)" stop-opacity="0.95"/>
          <stop offset="0.4" stop-color="var(--glow)" stop-opacity="0.85"/>
          <stop offset="1" stop-color="var(--ice)" stop-opacity="0.35"/>
        </radialGradient>
      </defs>
      <ellipse cx="190" cy="130" rx="150" ry="150" fill="url(#bulb-glow)"/>
    </svg>
    <div class="banner__text">
      <h1 class="banner__name">MARLOWE COLLEGE</h1>
      <p class="banner__tagline">state-of-the-art educational facility</p>
      <p class="banner__fields">Hospitality, Tourism, Business &amp; Management</p>
    </div>
  </div>
</body>
</html>
```